Bref créative
Business Cards/Stationary Vandorik Law, P.C.
Professional
Colvin R. Vandorik
Attorney & Counselor at Law
489 Pellham Avenue
Worcester, Massachusetts 01604
Colvin@Vandorik-example.com
www.Vandorik-example.com
I would also like designs to include letterhead and envelopes. Thank you.
Would like to list the areas of practice on the back, Workers' Compensation, Car Accidents, Personal Injury, Family Law, Criminal Law

```html
<!DOCTYPE html>
<html lang="en">
<head>
<meta charset="utf-8">
<title>Vandorik Law, P.C. — Stationery Set</title>
<link href="https://fonts.googleapis.com/css2?family=Cinzel:wght@600&family=Open+Sans:wght@400;600&display=swap" rel="stylesheet">
<style>
  :root {
    --board: #1b1c1e;
    --board-light: #2a2b2e;
    --paper: #ffffff;
    --paper-shade: #e9eaee;
    --navy: #1e2f7a;
    --navy-deep: #16245e;
    --ink: #3a3d47;
    --muted: #9a9ca3;
    --watermark: #eceef3;
    --label: #8d8f95;
  }
  * { box-sizing: border-box; margin: 0; padding: 0; }
  html, body { width: 1200px; height: 336px; overflow: hidden; }
  body {
    position: relative;
    background: radial-gradient(ellipse at 50% 30%, var(--board-light), var(--board) 70%);
    font-family: "Open Sans", sans-serif;
  }
  .piece { position: absolute; }
  .label {
    position: absolute; font-size: 6px; color: var(--label);
    text-align: center; letter-spacing: .3px;
  }

  /* brand block */
  .brand { left: 12px; top: 10px; display: flex; align-items: center; gap: 6px; }
  .brand-mark { width: 14px; height: 14px; background: var(--navy); }
  .brand-name {
    font-family: "Cinzel", serif; font-weight: 600; color: #c9cfe6;
    font-size: 13px; letter-spacing: .5px; line-height: 1;
  }
  .brand-sub { left: 12px; top: 52px; font-size: 6px; color: var(--label); }

  .wordmark {
    font-family: "Cinzel", serif; font-weight: 600; color: var(--navy);
    display: flex; align-items: center; gap: 3px; line-height: 1;
  }
  .wordmark i { display: inline-block; background: var(--navy); }

  /* business cards */
  .card { width: 72px; height: 43px; box-shadow: 0 1px 3px rgba(0,0,0,.6); }
  .card-front { left: 12px; top: 187px; background: var(--paper); padding: 5px; }
  .card-front .wordmark { font-size: 5px; }
  .card-front .wordmark i { width: 5px; height: 5px; }
  .card-front .details { margin-top: 6px; font-size: 2.4px; color: var(--ink); line-height: 1.35; text-align: right; }
  .card-back { left: 12px; top: 271px; background: var(--navy); padding: 5px; }
  .card-back .practice { font-size: 2.6px; color: #dfe4f5; line-height: 1.5; margin-top: 16px; }

  /* letterhead */
  .letterhead { width: 161px; height: 288px; top: 19px; background: var(--paper); box-shadow: 0 2px 6px rgba(0,0,0,.6); padding: 12px 14px; }
  .sheet-a { left: 216px; }
  .sheet-b { left: 427px; }
  .letterhead .head { display: flex; justify-content: space-between; align-items: flex-start; }
  .letterhead .wordmark { font-size: 6.5px; }
  .letterhead .wordmark i { width: 7px; height: 7px; }
  .letterhead .contact { font-size: 2.6px; color: var(--muted); line-height: 1.4; text-align: right; }
  .letterhead .rule { height: 1px; background: var(--navy); margin-top: 5px; opacity: .6; }
  .watermark { position: absolute; left: 45px; top: 90px; width: 72px; height: 72px; border-radius: 50%; background: var(--watermark); }

  /* envelopes */
  .envelope { width: 233px; height: 82px; background: var(--paper); box-shadow: 0 2px 6px rgba(0,0,0,.6); left: 643px; padding: 8px 10px; }
  .env-a { top: 115px; }
  .env-b { top: 213px; }
  .envelope .wordmark { font-size: 6px; }
  .envelope .wordmark i { width: 6px; height: 6px; }
  .envelope .return { font-size: 2.6px; color: var(--muted); margin-top: 3px; line-height: 1.4; }

  .env-backs { left: 900px; top: 22px; }
</style>
</head>
<body>

  <div class="piece brand">
    <span class="brand-mark"></span>
    <span class="brand-name">VANDORIK<br>LAW, P.C.</span>
  </div>
  <div class="piece brand-sub">Stationery Set</div>

  <div class="piece card card-front">
    <div class="wordmark"><i></i>VANDORIK LAW, P.C.</div>
    <div class="details">
      Colvin R. Vandorik<br>Attorney &amp; Counselor at Law<br>489 Pellham Avenue<br>Worcester, Massachusetts 01604<br>Colvin@Vandorik-example.com<br>www.Vandorik-example.com
    </div>
  </div>
  <div class="label" style="left:12px;top:234px;width:72px">Card Front</div>

  <div class="piece card card-back">
    <div class="practice">Workers' Compensation · Car Accidents<br>Personal Injury · Family Law · Criminal Law</div>
  </div>
  <div class="label" style="left:12px;top:318px;width:72px">Card Back</div>

  <div class="piece letterhead sheet-a">
    <div class="head">
      <div class="wordmark"><i></i>VANDORIK LAW, P.C.</div>
      <div class="contact">489 Pellham Avenue<br>Worcester, Massachusetts 01604<br>Colvin@Vandorik-example.com<br>www.Vandorik-example.com</div>
    </div>
    <div class="rule"></div>
    <div class="watermark"></div>
  </div>
  <div class="label" style="left:216px;top:312px;width:161px">Letterhead Page 1</div>

  <div class="piece letterhead sheet-b">
    <div class="head">
      <div class="wordmark"><i></i>VANDORIK LAW, P.C.</div>
      <div class="contact">489 Pellham Avenue<br>Worcester, Massachusetts 01604<br>Colvin@Vandorik-example.com<br>www.Vandorik-example.com</div>
    </div>
    <div class="rule"></div>
    <div class="watermark"></div>
  </div>
  <div class="label" style="left:427px;top:312px;width:161px">Letterhead Page 2</div>

  <div class="piece envelope env-a">
    <div class="wordmark"><i></i>VANDORIK LAW, P.C.</div>
    <div class="return">489 Pellham Avenue<br>Worcester, Massachusetts 01604</div>
  </div>
  <div class="piece envelope env-b">
    <div class="wordmark"><i></i>VANDORIK LAW, P.C.</div>
    <div class="return">489 Pellham Avenue<br>Worcester, Massachusetts 01604</div>
  </div>
  <div class="label" style="left:643px;top:302px;width:233px">Envelope Front</div>

  <svg class="piece env-backs" width="276" height="290" viewBox="0 0 276 290" aria-hidden="true">
    <!-- back with grey open flap -->
    <rect x="0" y="0" width="276" height="62" fill="var(--paper-shade)"/>
    <polygon points="0,0 138,40 276,0" fill="#cfd1d7"/>
    <!-- back with navy flap -->
    <rect x="0" y="78" width="276" height="96" fill="var(--paper)"/>
    <polygon points="0,78 138,128 276,78" fill="var(--navy)"/>
    <polyline points="0,174 138,134 276,174" fill="none" stroke="#d5d7dd" stroke-width="1"/>
    <!-- plain white back -->
    <rect x="0" y="188" width="276" height="96" fill="var(--paper)"/>
    <polygon points="0,188 138,232 276,188" fill="none" stroke="#d5d7dd" stroke-width="1"/>
    <polyline points="0,284 138,244 276,284" fill="none" stroke="#d5d7dd" stroke-width="1"/>
  </svg>
  <div class="label" style="left:900px;top:316px;width:276px">Envelope Back</div>

</body>
</html>
```